K7 Dynamics Stationery Design Project

We are looking to have stationary designs created for our company branding materials. We are looking for the following to be created.
1. Business Cards (front & back)
2. Letterhead
3. Envelopes #10
We are a new web design, development and marketing firm. Primary color scheme is desired to be blue/grey/white. This web start-up is owned and operated by individuals with 15+ years experience each in the industry so should not look as though it is a start-up by young/inexperienced individuals.
We build website & custom applications/software. In addition we provide the full spectrum of web marketing solutions including SEO, PPC, Social Media, Branding, Content Marketing and PR.
Please let us know if you have any questions. Looking forward to seeing all the amazing design ideas.
Attached is our logo.
Thanks!
Target Market(s)
Company will be nearly 100% business to business sales. Looking to work with companies that are already established, with a website, who want to take their website and/or online marketing efforts to the next level.
Industry/Entity Type
Marketing
Look and feel

```html
<!DOCTYPE html>
<html lang="en">
<head>
<meta charset="utf-8">
<title>K7 Dynamics — Business Card</title>
<link href="https://fonts.googleapis.com/css2?family=Jost:wght@400;500;600;700&display=swap" rel="stylesheet">
<style>
  :root {
    --page-bg: #3a3a3c;
    --card-white: #f7f7f6;
    --blue-light: #4dbbe8;
    --blue-mid: #2a9ad6;
    --blue-deep: #1470b8;
    --brand-blue: #1f86cc;
    --ink-dark: #3b3b3d;
    --ink-mid: #5a5a5c;
    --ink-soft: #8a8a8c;
  }
  * { margin: 0; padding: 0; box-sizing: border-box; }
  html, body {
    width: 1200px; height: 900px; overflow: hidden;
    background: var(--page-bg);
    font-family: "Jost", "Futura", sans-serif;
  }
  .stage {
    width: 1200px; height: 900px;
    display: flex; align-items: center; justify-content: center; gap: 40px;
  }
  .card {
    width: 540px; height: 309px; position: relative; overflow: hidden;
    box-shadow: 0 14px 30px rgba(0,0,0,.45);
  }

  /* Back of card */
  .card-back {
    background: radial-gradient(ellipse at 60% 35%, var(--blue-light) 0%, var(--blue-mid) 55%, var(--blue-deep) 100%);
    color: #fff;
  }
  .card-back .brand {
    position: absolute; left: 0; right: 0; top: 108px;
    display: flex; flex-direction: column; align-items: center;
  }
  .brand-row { display: flex; align-items: center; gap: 10px; }
  .brand-dot { width: 20px; height: 20px; border-radius: 50%; background: #fff; }
  .brand-name { font-weight: 700; font-size: 30px; letter-spacing: .5px; text-transform: uppercase; }
  .brand-tagline { font-size: 12.5px; margin-top: 2px; letter-spacing: .3px; }
  .card-back .web {
    position: absolute; left: 0; right: 0; bottom: 38px;
    text-align: center; font-size: 12px; letter-spacing: .4px; opacity: .95;
  }

  /* Front of card */
  .card-front { background: var(--card-white); color: var(--ink-dark); }
  .edge-dot {
    position: absolute; left: -14px; top: 48px;
    width: 30px; height: 30px; border-radius: 50%; background: var(--brand-blue);
  }
  .person { position: absolute; left: 34px; top: 44px; }
  .person-name { color: var(--brand-blue); font-size: 20px; font-weight: 500; letter-spacing: .3px; }
  .person-role { color: var(--ink-mid); font-size: 13px; margin-top: 1px; }
  .address {
    position: absolute; left: 34px; top: 160px;
    font-weight: 600; font-size: 13px; line-height: 1.3; color: var(--ink-dark);
  }
  .contacts {
    position: absolute; left: 34px; top: 208px;
    font-size: 13px; color: var(--ink-mid); line-height: 1.45;
  }
  .contact-line { display: flex; align-items: center; gap: 8px; }
  .contact-line svg { width: 13px; height: 11px; fill: var(--brand-blue); }
  .contacts .web { margin-top: 10px; font-weight: 500; color: var(--ink-dark); }
  .contacts .web span { color: var(--brand-blue); font-weight: 600; }
  .card-front .brand {
    position: absolute; right: 34px; top: 128px;
    display: flex; flex-direction: column; align-items: flex-end;
  }
  .card-front .brand-dot { background: var(--brand-blue); }
  .card-front .brand-name { font-size: 24px; color: var(--ink-dark); }
  .card-front .brand-tagline { font-size: 10.5px; color: var(--ink-dark); }
</style>
</head>
<body>
<main class="stage">
  <section class="card card-back" aria-label="Business card back">
    <div class="brand">
      <div class="brand-row"><span class="brand-dot"></span><span class="brand-name">K7 Dynamics</span></div>
      <div class="brand-tagline">Web Design, Development and Marketing</div>
    </div>
    <div class="web">www.k7dynamics.com</div>
  </section>

  <section class="card card-front" aria-label="Business card front">
    <span class="edge-dot"></span>
    <div class="person">
      <div class="person-name">Daniel Whitford</div>
      <div class="person-role">Position</div>
    </div>
    <address class="address" style="font-style:normal">1870 W. 96th Court<br>Lincoln, NE 68521</address>
    <div class="contacts">
      <div class="contact-line">
        <svg viewBox="0 0 13 11" aria-hidden="true"><path d="M1 3.5C1 1.5 3 1 6.5 1S12 1.5 12 3.5V5H9.5V3.8H3.5V5H1Z M3 6h7l1.5 4H1.5Z"/></svg>
        +12 3 555-0148
      </div>
      <div class="contact-line">
        <svg viewBox="0 0 13 11" aria-hidden="true"><path d="M0.5 1h12v9h-12Z M1.8 2.2v.4l4.7 3.3 4.7-3.3v-.4Z" fill-rule="evenodd"/></svg>
        info@k7dynamics.com
      </div>
      <div class="web">www.<span>k7dynamics</span>.com</div>
    </div>
    <div class="brand">
      <div class="brand-row"><span class="brand-dot"></span><span class="brand-name">K7 Dynamics</span></div>
      <div class="brand-tagline">Web Design, Development and Marketing</div>
    </div>
  </section>
</main>
</body>
</html>
```